We require a banner design for a 53' x 10' trailer for a future development to be displayed on the side of the highway. The development name is 712 35 Commerce Park, logo is attached. This is an industrial future development. Please also include the RLW Group logo and MERO Development logos as well.

Industry/Entity Type

Real Estate / Construction / Developer / Industrial Future Development

Requirements
Must have
• Logos provided

```html
<!DOCTYPE html>
<html lang="en">
<head>
<meta charset="utf-8">
<title>712 35 Commerce Park – Trailer Banner</title>
<link href="https://fonts.googleapis.com/css2?family=Krona+One&family=Michroma&display=swap" rel="stylesheet">
<style>
  :root {
    --page-bg: #e9edf0;
    --panel-light: #e6e5e8;
    --panel-dark: #0d0b0a;
    --ink: #111010;
    --text-light: #f2f2f2;
    --accent-brown: #6b5a4c;
    --accent-red: #d3202f;
    --pill-bg: #ebebed;
  }
  * { margin: 0; padding: 0; box-sizing: border-box; }
  html, body {
    width: 1200px;
    height: 844px;
    overflow: hidden;
    background: var(--page-bg);
  }
  .banner {
    position: absolute;
    left: 20px;
    top: 257px;
    width: 1160px;
    height: 330px;
    display: flex;
    overflow: hidden;
  }
  .brand-panel {
    width: 355px;
    background: var(--panel-light);
    display: flex;
    flex-direction: column;
    justify-content: center;
    padding-left: 36px;
  }
  .brand-number {
    font-family: "Krona One", sans-serif;
    font-size: 86px;
    line-height: 1;
    color: var(--ink);
    letter-spacing: -2px;
  }
  .brand-number + .brand-number { margin-top: 6px; }
  .brand-number--lower {
    display: flex;
    align-items: center;
    gap: 20px;
  }
  .brand-dot {
    width: 58px;
    height: 58px;
    border-radius: 50%;
    background: var(--accent-brown);
    flex: none;
  }
  .title-panel {
    position: relative;
    flex: 1;
    background: var(--panel-dark);
    padding: 58px 0 0 30px;
  }
  .project-title {
    font-family: "Michroma", sans-serif;
    font-weight: 400;
    font-size: 74px;
    line-height: 1.08;
    color: var(--text-light);
    letter-spacing: 2px;
  }
  .partner-strip {
    position: absolute;
    right: 0;
    bottom: 40px;
    width: 390px;
    height: 80px;
    background: var(--pill-bg);
    border-radius: 30px 0 0 30px;
    display: flex;
    align-items: center;
    justify-content: space-around;
    padding-left: 16px;
  }
  .partner {
    display: flex;
    align-items: center;
    gap: 8px;
    font-family: "Michroma", sans-serif;
    font-size: 15px;
    color: var(--ink);
  }
  .partner-square {
    width: 14px;
    height: 14px;
    background: var(--accent-red);
  }
</style>
</head>
<body>
  <div class="banner">
    <div class="brand-panel">
      <div class="brand-number">712</div>
      <div class="brand-number brand-number--lower">
        <span class="brand-dot"></span>35
      </div>
    </div>
    <div class="title-panel">
      <h1 class="project-title">COMMERCE<br>PARK</h1>
      <div class="partner-strip">
        <div class="partner">MERO Development</div>
        <div class="partner"><span class="partner-square"></span>RLW Group</div>
      </div>
    </div>
  </div>
</body>
</html>
```